Zielgruppe
Die Kessler-Volkshochschule Kreis Aurental ist eine gemeinnützige Einrichtung zur Erwachsenen- und Weiterbildung mit ca. 5.000 Veranstaltungen pro Jahr.
Volkshochschulen sind entgegen ihrer Bezeichnung keine Hochschulen oder Schulen, sondern in Deutschland dem Bildungsbereich der Weiterbildung zugeordnet.
Aufgabenstellung
Die Kessler-Volkshochschule Kreis Aurental möchte mit einer neuen Webseite, welche auch für mobile Geräte geeignet sein muss, Ihren neuen Internetauftritt umsetzen.
Vorgaben:
- der Internetauftritt soll modern gestaltet sein.
- die unter Dateien befindlichen Guidelines müssen eingehalten werden. Wichtig hierbei ist, dass die 6 Symbole auf die Startseite für die Auswahl der jeweiligen Kursbereiche integriert werden. Hierbei ist zu beachten, dass die Anzahl der Symbole erweiterbar ist.
Als CMS wird Typo3 genutzt.
Es geht um die Erstellung der Startseite auf welcher auch News untergebracht werden sollen - ggf. in Kachelform. Und die Erstellung einer Unterseite.

```html
<!DOCTYPE html>
<html lang="en">
<head>
<meta charset="utf-8">
<title>Kessler-Volkshochschule Kreis Aurental</title>
<link href="https://fonts.googleapis.com/css2?family=Open+Sans:wght@400;600;800&family=Patrick+Hand&display=swap" rel="stylesheet">
<style>
:root{
  --navy:#0b3467;
  --navy-dark:#082a55;
  --page:#4b4b4b;
  --white:#ffffff;
  --panel:#e3e3e3;
  --frame:#5a5a5a;
  --text-blue:#1b3f7a;
  --grey-text:#6b6b6b;
  --beruf:#6bbfe8;
  --kultur:#e0161d;
  --gesell:#e8680f;
  --sprachen:#8a55a3;
  --gesund:#a6c71b;
  --grund:#f2b516;
}
*{box-sizing:border-box;margin:0;padding:0}
html,body{width:1200px;height:1180px;overflow:hidden}
body{position:relative;background:var(--page);font-family:"Open Sans",Arial,sans-serif}
.abs{position:absolute}
.header{left:0;top:0;width:1200px;height:84px;background:var(--white);box-shadow:0 3px 6px rgba(0,0,0,.35);z-index:2}
.brand{left:96px;top:14px;display:flex;align-items:center;gap:14px}
.brand-dot{width:42px;height:42px;border-radius:50%;background:var(--navy)}
.brand-name{font-size:22px;font-weight:400;color:var(--navy);line-height:25px;border-left:1px solid #bbb;padding-left:14px}
.lang{left:915px;top:10px;width:140px;height:22px;background:#d9d9d9;font-size:12px;color:#333;padding:3px 8px}
.lang::after{content:"";position:absolute;right:0;top:0;width:22px;height:22px;background:#555}
.lang-arrow{right:6px;top:9px;width:0;height:0;border-left:5px solid transparent;border-right:5px solid transparent;border-top:6px solid #fff;z-index:1}
.utility{right:147px;top:47px;font-size:12px;color:var(--text-blue);word-spacing:2px}
.utility span{margin:0 10px}
.nav{left:0;top:84px;width:1200px;height:48px;background:var(--navy);display:flex;padding-left:118px}
.nav a{color:var(--white);text-decoration:none;font-size:14.5px;height:48px;line-height:48px;padding:0 31px;border-right:1px solid #052146}
.nav a:last-child{border:none;padding-left:40px}
.main{left:100px;top:132px;width:995px;height:883px;background:var(--white)}
.hero{left:124px;top:133px;width:946px;height:378px;background:linear-gradient(180deg,#b9d5ef 0%,#e4eef7 30%,#4a78b8 50%,#2e6a4a 70%,#8a7a60 100%);box-shadow:0 30px 25px -18px rgba(0,0,0,.45)}
.hero-caption{left:100px;top:390px;width:412px;height:97px;background:var(--navy);color:var(--white);text-align:center}
.hero-caption h1{font-family:"Patrick Hand",cursive;font-weight:400;font-size:34px;margin-top:12px}
.hero-caption p{font-family:Arial,sans-serif;font-size:16px;margin-top:2px}
.hero-fold{left:100px;top:368px;width:0;height:0;border-left:22px solid transparent;border-bottom:22px solid #111}
.slider{left:946px;top:395px;width:98px;height:98px;background:rgba(150,150,150,.7);color:#ddd;font-size:64px;text-align:center;line-height:90px;letter-spacing:4px}
.topics{left:124px;top:580px;width:947px;height:195px;background:var(--panel)}
.topic{position:absolute;width:280px;height:78px;border-radius:3px;color:var(--white);font-weight:800;font-size:25px;display:flex;align-items:center;padding-left:14px;gap:16px;text-shadow:0 1px 2px rgba(0,0,0,.4)}
.topic .icon{width:60px;height:50px;background:rgba(255,255,255,.25);border-radius:3px;flex:none}
.topic .label{margin-left:auto;margin-right:auto}
.beruf{left:11px;top:11px;background:var(--beruf)}
.kultur{left:331px;top:11px;background:var(--kultur)}
.gesellschaft{left:656px;top:11px;background:var(--gesell)}
.sprachen{left:11px;top:103px;background:var(--sprachen)}
.gesundheit{left:331px;top:103px;background:var(--gesund)}
.grundbildung{left:656px;top:103px;background:var(--grund);font-size:22px}
.card{top:815px;width:294px;height:180px;background:var(--frame);padding:10px}
.card-photo{position:relative;width:100%;height:100%}
.card-text{position:absolute;left:0;right:0;bottom:0;height:80px;background:rgba(255,255,255,.78);font-family:Arial,sans-serif;font-size:12.5px;line-height:16px;color:#111;padding:10px 14px}
.card-1{left:124px}.card-1 .card-photo{background:linear-gradient(180deg,#c9d6e2,#b59a7a)}
.card-2{left:451px}.card-2 .card-photo{background:linear-gradient(180deg,#6f8f55,#c8b9a8)}
.card-3{left:777px}.card-3 .card-photo{background:linear-gradient(90deg,#a84a4a,#6c8db3 60%,#d9c5b0)}
.footer{left:0;top:1015px;width:1200px;height:165px;background:var(--navy);color:var(--white)}
.footer-nav{position:absolute;left:0;top:15px;width:1200px;text-align:center;font-size:14.5px;word-spacing:2px}
.footer-nav span{margin:0 26px}
.footer-rule{position:absolute;left:60px;top:53px;width:1020px;height:1px;background:#24497a}
.copyright{position:absolute;left:123px;top:110px;font-size:14.5px}
.find{position:absolute;left:820px;top:112px;font-size:19px;letter-spacing:1px}
.social{position:absolute;top:104px;width:40px;height:40px;border-radius:3px}
.s1{left:955px;background:#12a9e0}.s2{left:1005px;background:#3b5897}.s3{left:1055px;background:#1da1f2}
</style>
</head>
<body>
<header class="header abs">
  <div class="brand abs">
    <span class="brand-dot" aria-hidden="true"></span>
    <span class="brand-name">Kessler-Volkshochschule<br>Kreis Aurental</span>
  </div>
  <div class="lang abs">Language<span class="lang-arrow abs"></span></div>
  <div class="utility abs">(012) 345-6789<span>|</span>Student Portal<span>|</span>Staff Portal</div>
</header>
<nav class="nav abs">
  <a>INDEX</a><a>ABOUT</a><a>PROGRAMS</a><a>ADMISSIONS</a><a>LOCATIONS</a><a>FINANCIAL AID</a><a>STUDENTS</a>
</nav>
<main class="main abs"></main>
<div class="hero abs" role="img" aria-label="Hiker with backpack standing on a rocky summit above wooded blue mountains"></div>
<div class="hero-fold abs"></div>
<div class="hero-caption abs">
  <h1>College District Aurental</h1>
  <p>Germany associated with the education of training</p>
</div>
<div class="slider abs">‹›</div>
<section class="topics abs">
  <a class="topic beruf"><span class="icon" role="img" aria-label="Career icon"></span><span class="label">BERUF</span></a>
  <a class="topic kultur"><span class="icon" role="img" aria-label="Culture icon"></span><span class="label">KULTUR</span></a>
  <a class="topic gesellschaft"><span class="icon" role="img" aria-label="Society icon"></span><span class="label">GESELLSCHAFT</span></a>
  <a class="topic sprachen"><span class="icon" role="img" aria-label="Languages icon"></span><span class="label">SPRACHEN</span></a>
  <a class="topic gesundheit"><span class="icon" role="img" aria-label="Health icon"></span><span class="label">GESUNDHEIT</span></a>
  <a class="topic grundbildung"><span class="icon" role="img" aria-label="Basic education icon"></span><span class="label">GRUNDBILDUNG</span></a>
</section>
<article class="card card-1 abs"><div class="card-photo" role="img" aria-label="Two students talking outdoors in front of a historic building"><p class="card-text">Kessler International College is a place to learn, connect, strive, and achieve. The faculty and staff care about YOUR success</p></div></article>
<article class="card card-2 abs"><div class="card-photo" role="img" aria-label="Smiling student on a leafy campus path with classmates behind"><p class="card-text">Kessler International College MBA programs offer students the opportunity to exchange ideas</p></div></article>
<article class="card card-3 abs"><div class="card-photo" role="img" aria-label="Student choosing a book between library shelves"><p class="card-text">With traveling, work and school, I had to learn time management the best way I can.</p></div></article>
<footer class="footer abs">
  <div class="footer-nav">Home<span>|</span>About Us<span>|</span>Programs<span>|</span>Admissions<span>|</span>Locations<span>|</span>Financial Aid<span>|</span>Students</div>
  <div class="footer-rule"></div>
  <p class="copyright">Copyright 2014. All Rights Reserved</p>
  <p class="find">Find Us On:</p>
  <span class="social s1" role="img" aria-label="Chat profile"></span>
  <span class="social s2" role="img" aria-label="Social network page"></span>
  <span class="social s3" role="img" aria-label="News feed profile"></span>
</footer>
</body>
</html>
```